Web Design Project for Weightwise Alliance

Aim
As the peak body on obesity, to be the ‘go to website’ for information about obesity and for people that are overweight or obese. Whether an individual looking for support and advice; a professional such as a dietician or a medical practitioner; an academic researcher studying the field; a related organisation specialising in cancer; diabetes or cardio issues or a policy maker
Requirements
A professional site that is compatible for viewing on PCs Mac, ipads and iphones
To include the following:
• Announcements bar – (for adding in conferences, news grabs etc)
• Search tool (for academic’s papers, terms in fact sheets)
• Secure log in (for KRP & WA directors & staff personnel for board papers etc)
• Good visuals including changing photos (should be engaging for public – see sample)
• Web sharing apps Email/circlenet login and other social media; like button
• Get involved – to express interest in conferences; potential sponsors
• Ebulletin (KRP)- subscribe - emailed to a database or posted to a social media site
• WA Recommended Apps - DLQ, VORN, Plateloggr? T&K
• WA blog
• Capture database of emails/enquiries for ebulletin and fact sheets
Contents
Landing page – containing aspects above (announcements, search tool, visuals, social media tools, get involved button, recommended apps);
Mission statement and logo with words ‘insight and momentum’ prominently displayed
Sections
1. About WA - Who we are – Weightwise Alliance Board and Expert Review Panel cvs; CEO and research officer – annual report
2. For General Public - The big questions about obesity – the interaction of food (protein & fructose), exercise, epigenetics “its not your fault”, hormones (eg leptin) & metabolism. The Fact Sheets; simple summaries of latest research?
3. For Professionals - Expert Review Panel - KRP Ebulletins - Research and Publications
4. Media and latest news on obesity
5. Support WA in its mission– get involved – note DGR status etc.
6. Website terms of use – Halvers to provide disclaimers etc
For later - professionals – Post Conference youtubes
- general public – anti-obesity app
Websites we like:
- http://www.sugarscalehub.com
- www.bellytrust.org.au
- http://www.tallo.org/international - clean lines; well organised
- http://www.verdal.org/ good layout of tabs about us, news and media, science, login, myverdalpage
- http://www.rallyzone.co.uk/sport innovate way to promote fitness
We would also be keen to get the site coded so would like an estimate of how much it would cost to create the html version of the site also with css for the main styles.

```html
<!DOCTYPE html>
<html lang="en">
<head>
<meta charset="utf-8">
<title>Weightwise Alliance</title>
<link href="https://fonts.googleapis.com/css2?family=Jost:wght@300;400;500&family=PT+Sans:wght@400;700&display=swap" rel="stylesheet">
<style>
:root{
  --teal:#1aaec3;
  --navy:#1d3a78;
  --text:#222;
  --nav:#555;
  --muted:#8a8a8a;
  --rule:#dcdcdc;
  --bar:#e4e4e4;
  --head-top:#e6ecf8;
  --white:#fff;
}
*{margin:0;padding:0;box-sizing:border-box}
html,body{width:1200px;height:3428px;overflow:hidden;background:var(--white)}
body{position:relative;font-family:"PT Sans",sans-serif;color:var(--text)}
.site-header{position:absolute;left:0;top:0;width:1200px;height:1140px;
  background:linear-gradient(to bottom,var(--head-top) 0,var(--white) 520px);
  border-bottom:3px solid var(--rule)}
.brand{position:absolute;top:45px;left:0;width:1200px;text-align:center}
.brand-mark{display:block;margin:0 auto;width:150px;height:150px;border-radius:50%;background:var(--navy)}
.brand-name{display:block;margin-top:42px;font-family:"Jost",sans-serif;font-weight:400;font-size:74px;line-height:1;color:var(--teal)}
.brand-tagline{display:block;margin-top:16px;font-family:"Jost",sans-serif;font-size:36px;letter-spacing:5px;color:var(--navy)}
.main-nav{position:absolute;top:446px;left:0;width:1200px;list-style:none;text-align:center;font-family:"Jost",sans-serif;font-size:47px;color:var(--nav)}
.main-nav li{height:90px;line-height:90px}
.main-nav .active{color:var(--teal)}
.main-nav .login{font-size:42px;color:#666}
.main-nav .login svg{margin-right:22px;vertical-align:middle}
.hero-photo{position:absolute;left:60px;top:1219px;width:1084px;height:559px;border-radius:12px;
  border:3px solid #e8e8e8;box-shadow:0 3px 10px rgba(0,0,0,.08);
  background:linear-gradient(135deg,#fafafa 0,#f1efee 55%,#e8e4e2 100%)}
.intro{position:absolute;left:60px;top:1824px;width:1090px}
.intro h1{font-family:"Jost",sans-serif;font-weight:300;font-size:84px;line-height:112px;color:#111}
.intro h1 em{font-style:normal;color:var(--teal)}
.intro p{margin-top:12px;font-size:49px;line-height:60px;color:var(--muted)}
.glow{position:absolute;left:260px;top:2360px;width:700px;height:90px;border-radius:50%;
  background:radial-gradient(ellipse at center top,rgba(0,0,0,.07),rgba(0,0,0,0) 70%)}
.news{position:absolute;left:60px;top:2470px;width:1084px}
.news h2{font-family:"Jost",sans-serif;font-weight:400;font-size:64px;line-height:80px;color:#111}
.news .bar{margin-top:58px;height:15px;background:var(--bar)}
.news h3{margin-top:30px;font-weight:400;font-size:49px;line-height:64px;color:#111}
.news .meta{margin-top:28px;font-size:38px;line-height:45px;color:var(--muted)}
.news .meta a{color:var(--teal);text-decoration:none}
.social{position:absolute;top:3080px;left:0;width:1200px;text-align:center;font-family:"PT Sans",sans-serif;font-weight:700;font-size:58px;color:#8c8c8c}
.social span{margin:0 40px}
.site-footer{position:absolute;left:0;top:3210px;width:1200px;height:218px;border-top:3px solid var(--rule);
  text-align:center;font-size:41px;color:#666;padding-top:70px}
</style>
</head>
<body>
<header class="site-header">
  <div class="brand">
    <span class="brand-mark"></span>
    <span class="brand-name">Weightwise Alliance</span>
    <span class="brand-tagline">insight and momentum</span>
  </div>
  <ul class="main-nav">
    <li>About WA</li>
    <li class="active">For General Public</li>
    <li>For Professionals</li>
    <li>Latest News</li>
    <li>Support WA</li>
    <li>Terms of Use</li>
    <li class="login"><svg width="14" height="20" viewBox="0 0 14 20"><path d="M0 0L14 10L0 20Z" fill="#1aaec3"/></svg>Secure Login</li>
  </ul>
</header>

<div class="hero-photo" role="img" aria-label="Photo of a woman in black sportswear doing a seated exercise on a white background"></div>

<section class="intro">
  <h1>Obesity and for people that are <em>overweight</em> or obese</h1>
  <p>Lorem ipsum dolor sit amet, consectetuer adipiscing elit, sed diam nonummy nibh euismod tincidunt ut laoreet dolore magna aliquam erat volutpat.</p>
</section>

<div class="glow"></div>

<section class="news">
  <h2>Latest News</h2>
  <div class="bar"></div>
  <h3>Your Chance to ask Council Chair Halden Mirov a question!</h3>
  <p class="meta">MAY, 4 2012<br>Posted by <a href="#">Tobias Renwick</a></p>
</section>

<nav class="social"><span>chirply</span><span>Streamly</span><span>circlenet</span></nav>

<footer class="site-footer">© 2011 Weightwise Alliance. All right reserved</footer>
</body>
</html>
```